Postcard Designs - Brenlow and Corvane

We are a locally owned, family operated pool service and repair company. The postcards we want to have designed is to co-market with two different companies (Brenlow and Corvane) . Both companies manufacture variable speed pumps. We are looking for customers who want to upgrade their systems to save $ on energy costs.

Both postcards are basically the same (and can use the same image rather than 2 different like I have in the Word doc). We just need to modify the text and company logo.

Postcard Specs

Full Bleed Size (starting document size)
8.64" x 5.59"
219 x 142 mm
2592 x 1677 pixels
* Finished artwork should use the full bleed dimensions for best results.
Document Trim Size (final size after being cut)
8.52" x 5.47"
216 x 139 mm
2556 x 1642 pixels
* Please be sure to keep all text within the safe margin.
Resolution
300 DPI

Target Market(s)

Adults in Northern California ages 30 - 80 that make the buying decisions for their families.

Industry/Entity Type

Pool Service

Font styles to use
Sans Serif

Colors
33a6d7
3277b5
acd037
fece3e

Requirements
Must have
• - company logo
- detail on variable speed pump
- cost savings chart
- image of family having fun (something related to the question on the front of the postcard - what would you do with $100/month?)

```html
<!DOCTYPE html>
<html lang="en">
<head>
<meta charset="utf-8">
<title>Brenlow Variable Speed Pumps Postcard</title>
<link rel="stylesheet" href="https://fonts.googleapis.com/css2?family=Alegreya+Sans:wght@400&family=Open+Sans:wght@400;700;800&display=swap">
<style>
  :root {
    --page-bg: #e9e6e1;
    --brand-blue: #2fa3d9;
    --deep-blue: #2a6fb6;
    --logo-blue: #1f6bbf;
    --white: #ffffff;
    --ink: #111111;
    --sky-top: #1c4f8f;
    --sky-mid: #2f68ad;
    --sky-low: #6f9fd0;
    --sea-deep: #1fb3b6;
    --sea: #46d3c8;
    --foam: #d8efe9;
    --sand: #f3eee6;
    --sand-low: #e7dfd1;
  }
  html, body {
    margin: 0;
    width: 1200px;
    height: 878px;
    overflow: hidden;
    background: var(--page-bg);
  }
  .postcard {
    position: absolute;
    left: 87px;
    top: 99px;
    width: 1023px;
    height: 661px;
    box-shadow: 0 6px 18px rgba(0,0,0,0.2);
  }
  .headline {
    font-family: "Alegreya Sans", sans-serif;
    font-size: 41px;
    fill: var(--white);
  }
  .brand-name {
    font-family: "Open Sans", sans-serif;
    font-weight: 800;
    font-size: 45px;
    fill: var(--logo-blue);
  }
  .brand-tagline {
    font-family: "Open Sans", sans-serif;
    font-weight: 700;
    font-size: 20px;
    fill: var(--ink);
  }
  .savings-copy {
    font-family: "Open Sans", sans-serif;
    font-size: 24px;
    fill: var(--white);
  }
</style>
</head>
<body>
<svg class="postcard" viewBox="0 0 1023 661" xmlns="http://www.w3.org/2000/svg">
  <defs>
    <linearGradient id="beach-scene" x1="0" y1="0" x2="0" y2="1">
      <stop offset="0" stop-color="var(--sky-top)"/>
      <stop offset="0.25" stop-color="var(--sky-mid)"/>
      <stop offset="0.42" stop-color="var(--sky-low)"/>
      <stop offset="0.44" stop-color="var(--sea-deep)"/>
      <stop offset="0.6" stop-color="var(--sea)"/>
      <stop offset="0.7" stop-color="var(--foam)"/>
      <stop offset="0.8" stop-color="var(--sand)"/>
      <stop offset="1" stop-color="var(--sand-low)"/>
    </linearGradient>
  </defs>

  <rect class="hero-photo" x="0" y="0" width="1023" height="516" fill="url(#beach-scene)"
        role="img" aria-label="Photo of a family enjoying a tropical beach: parents walking arm in arm on white sand while two children run along the turquoise water"/>

  <path class="header-swoosh" d="M28,0 Q520,70 1023,203 L1023,0 Z" fill="var(--brand-blue)"/>
  <path class="header-swoosh-line" d="M28,0 Q520,70 1023,203" fill="none" stroke="var(--white)" stroke-width="3"/>

  <text class="headline" x="993" y="51" text-anchor="end">What would you do with…</text>
  <text class="headline" x="996" y="99" text-anchor="end">…$50-$100/month?</text>

  <rect class="divider-strip" x="0" y="515" width="1023" height="5" fill="var(--deep-blue)"/>

  <rect class="logo-panel" x="0" y="520" width="441" height="141" fill="var(--white)"/>
  <rect class="logo-square" x="58" y="551" width="50" height="50" fill="var(--logo-blue)"/>
  <text class="brand-name" x="118" y="597" textLength="258" lengthAdjust="spacingAndGlyphs">BRENLOW</text>
  <text class="brand-tagline" x="145" y="618" textLength="230" lengthAdjust="spacingAndGlyphs">Variable Speed Pumps</text>

  <rect class="savings-panel" x="441" y="520" width="582" height="141" fill="var(--brand-blue)"/>
  <text class="savings-copy" x="508" y="559">Moving to a variable speed pump saves</text>
  <text class="savings-copy" x="508" y="591">an average of $50 - $100/month on your</text>
  <text class="savings-copy" x="508" y="623">energy bill.</text>
</svg>
</body>
</html>
```